Exciting Wordpress Project: New Consulting Firm

A wordpress design is needed for my new consulting company, Brellow Advisory.

The site should have a modern feel to it and use the colour scheme from the attached 3 vector files.

I only know a little about Wordpress but the site should be mobile friendly.

The following menu options should be created:
1. Home
2. Brellow service lines (with sub-menus)
3. Our people
4. Brellow case studies
5. The Brellow story
6. Contact Brellow
Updates

Project Deadline Extended
Reason: Allow just one or two more designs to come in before deciding.

Target Market(s)

Government departments and medium private sector organisations

Industry/Entity Type

It Company

Requirements
Must have
• 1. Inclue Brellow logo at top of each page
2. Slider on the home page
3. Global navigation
4. Drop down navigation
5. Social media links
6. Search and contact details at the top of the home page
7. Home page to fit on one screen
8. Terms & Conditions, Privacy Policy at the bottom of the home page
9. Newsletter (i.e. postwren) subscription on home page
Nice to have
• 1. Background watermark from the Brellow logo
2. A layout similar to the photo attached - however open to different ideas

```html
<!DOCTYPE html>
<html lang="en">
<head>
<meta charset="utf-8">
<title>Brellow Advisory</title>
<link href="https://fonts.googleapis.com/css2?family=Source+Sans+3:wght@400;600;700&display=swap" rel="stylesheet">
<style>
:root{
  --bar:#616161;
  --ink:#2b2b2b;
  --muted:#5a5a5a;
  --logo:#6b6e73;
  --blue:#22509e;
  --blue-dark:#173d80;
  --blue-text:#274f98;
  --line:#d9d9d9;
  --panel:#eeeff1;
  --red:#e2401d;
  --footer:#2e2e2e;
  --wm:#ededee;
}
*{box-sizing:border-box;margin:0;padding:0}
html,body{width:920px;height:1200px;overflow:hidden;background:#fff}
body{position:relative;font-family:"Source Sans 3",sans-serif;color:var(--ink)}
.abs{position:absolute}
.top-bar{left:0;top:0;width:920px;height:12px;background:var(--bar)}
.brand{left:80px;top:42px;color:var(--logo);font-weight:600;line-height:1}
.brand .name{font-size:50px;letter-spacing:2px;display:block}
.brand .sub{font-size:15px;letter-spacing:17px;display:block;margin-top:6px;padding-left:4px}
.search{left:672px;top:61px;width:181px;height:31px;border:1px solid #c9c9c9;border-radius:4px;font-size:11px;font-style:italic;color:#9a9a9a;padding:8px 11px}
.search svg{position:absolute;right:9px;top:9px}
.main-nav{left:64px;top:144px;width:790px;height:37px;border-radius:4px;background:linear-gradient(#2d5fae,var(--blue-dark));display:flex;justify-content:space-between;align-items:center;padding:0 14px;box-shadow:0 2px 3px rgba(0,0,0,.25)}
.main-nav a{color:#fff;text-decoration:none;font-size:13px;letter-spacing:.2px}
.slider{left:65px;top:199px;width:789px;height:304px;background:linear-gradient(110deg,#c6d2e3 0%,#e9eef5 35%,#d9dee6 55%,#2c3d63 75%,#1d2f57 100%);overflow:hidden}
.slider-shadow{left:20px;top:498px;width:880px;height:26px;background:radial-gradient(ellipse at center top,rgba(0,0,0,.28),rgba(0,0,0,0) 70%)}
.caption{left:65px;top:414px;width:441px;height:66px;background:rgba(235,235,238,.82);padding:10px 22px}
.caption h2{font-weight:400;font-size:14px;color:#333;letter-spacing:.2px}
.caption p{font-size:10.5px;margin-top:9px;color:#222}
.dots{left:434px;top:516px;display:flex;gap:4px}
.dots span{width:16px;height:16px;border-radius:50%;background:radial-gradient(#e2e2e2,#bdbdbd);border:1px solid #d6d6d6}
.dots span.on{background:radial-gradient(#777,#4b4b4b)}
.watermark{left:60px;top:700px;width:800px;color:var(--wm);font-weight:700;line-height:1}
.watermark .w1{font-size:160px;letter-spacing:16px;display:block;text-align:center}
.watermark .w2{font-size:48px;letter-spacing:52px;display:block;text-align:center;margin-top:-8px;font-weight:400}
.card{width:230px;height:129px;top:558px;border:1px solid var(--line);background:#fff;box-shadow:0 6px 6px -4px rgba(0,0,0,.12)}
.card .label{position:absolute;left:2px;top:13px;width:157px;height:30px;background:var(--blue);color:#fff;font-size:12.5px;padding:7px 16px}
.card p{position:absolute;left:4px;top:58px;width:222px;font-size:10.5px;line-height:19px;color:#222}
.card .more{position:absolute;left:60px;top:117px;width:100px;height:28px;border:1px solid #cfcfcf;border-radius:3px;background:linear-gradient(#f7f7f7,#e2e2e2);color:#777;font-size:13.5px;text-align:center;line-height:26px;letter-spacing:.4px}
.welcome-title{left:64px;top:746px;font-size:17px;font-weight:400;color:#222}
.welcome-photo{left:64px;top:781px;width:160px;height:91px;background:linear-gradient(180deg,#6d8fb9,#c7d6e6 65%,#9aa6b1)}
.welcome-text{left:240px;top:777px;width:418px;font-size:10.5px;line-height:16.5px;color:#333}
.newsletter{left:691px;top:754px;width:162px;height:118px;background:var(--panel)}
.newsletter .t1{position:absolute;left:15px;top:7px;font-size:14px;color:var(--blue-text)}
.newsletter .t2{position:absolute;right:10px;top:28px;font-size:18px;color:var(--blue-text)}
.newsletter .field{position:absolute;left:15px;top:59px;width:105px;height:20px;background:#fff;border:1px solid #d5d5d5;font-size:10px;color:#888;padding:3px 6px}
.newsletter .submit{position:absolute;left:98px;top:89px;width:45px;height:14px;background:var(--red);color:#fff;font-size:9px;text-align:center;line-height:14px}
.divider{left:64px;top:915px;width:790px;height:1px;background:linear-gradient(90deg,#f1f1f1,#dedede,#f1f1f1)}
.tabs{left:64px;top:934px;width:292px;height:146px;border:1px solid var(--line)}
.tab{position:absolute;top:-1px;height:33px;font-size:10.5px;padding:9px 6px}
.tab.plain{left:-1px;width:66px;border:1px solid var(--line);border-bottom:none;background:#fff;color:#333}
.tab.active{left:74px;width:70px;background:#3f6fb3;color:#fff;top:0}
.tab-arrows{left:327px;top:943px;display:flex;gap:1px}
.arrow-btn{width:12px;height:12px;border-radius:50%;background:#c6c6c6;border:1px solid #b2b2b2;display:flex;align-items:center;justify-content:center}
.mission-photo{left:72px;top:978px;width:94px;height:89px;background:linear-gradient(#f4f4f4,#d8dbe0);border:1px solid #e3e3e3}
.mission-text{left:177px;top:977px;width:172px;font-size:10.5px;line-height:16.5px;color:#333}
.calendar{left:397px;top:935px;width:151px;height:143px;border:1px solid #dcdcdc;background:#fff}
.cal-head{height:22px;background:#3d3d3d;color:#fff;font-size:8px;display:flex;justify-content:space-between;align-items:center;padding:0 8px}
.calendar table{width:100%;border-collapse:collapse;table-layout:fixed}
.calendar th{font-size:4.5px;color:#888;font-weight:400;height:9px}
.calendar td{font-size:6px;text-align:center;height:21.6px;border:1px solid #e4e4e4;color:#333}
.calendar td.other{color:#aaa}
.calendar td.today{background:#2b62d6;color:#fff}
.news{left:603px;top:930px;width:251px}
.news h3{font-weight:400;font-size:14.5px;color:#222}
.news-arrows{left:805px;top:932px;display:flex;gap:1px}
.news-arrows .arrow-btn{width:14px;height:14px}
.news-item{margin-top:11px;font-size:10.5px;line-height:16.5px;color:#222}
.news-item b{font-weight:700}
.news-item + .news-item{margin-top:10px}
.footer{left:0;top:1132px;width:920px;height:68px;background:var(--footer);color:#eee}
.footer .copy{position:absolute;left:68px;top:29px;font-size:10.5px}
.social{position:absolute;left:732px;top:22px;display:flex;gap:9px}
.social span{width:24px;height:24px;border-radius:3px;background:#f1f1f1}
</style>
</head>
<body>
<div class="abs top-bar"></div>

<div class="abs brand" aria-label="Brellow Advisory">
  <span class="name">BRELLOW</span>
  <span class="sub">ADVISORY</span>
</div>

<div class="abs search">Search..
  <svg width="11" height="11" viewBox="0 0 11 11"><circle cx="4.5" cy="4.5" r="3.5" fill="none" stroke="#999" stroke-width="1.5"/><line x1="7" y1="7" x2="10" y2="10" stroke="#999" stroke-width="1.6"/></svg>
</div>

<nav class="abs main-nav">
  <a href="#">HOME</a>
  <a href="#">BRELLOW SERVICE LINES</a>
  <a href="#">OUR PEOPLE</a>
  <a href="#">BRELLOW CASE STUDIES</a>
  <a href="#">THE BRELLOW STORY</a>
  <a href="#">CONTACT BRELLOW</a>
</nav>

<div class="abs slider-shadow"></div>
<div class="abs slider" role="img" aria-label="Business team in suits working together at a meeting table, office windows behind"></div>
<div class="abs caption">
  <h2>CONTRARY TO POPULAR BELIEF, LOREM IPSM</h2>
  <p>Lorem Ipsum is simply dummy text of the printing and typesetting industry.</p>
</div>
<div class="abs dots"><span class="on"></span><span></span><span></span><span></span></div>

<div class="abs watermark" aria-hidden="true">
  <span class="w1">BRELLOW</span>
  <span class="w2">ADVISORY</span>
</div>

<section class="abs card" style="left:64px">
  <div class="label">OUR SERVICES</div>
  <p>Lorem Ipsum is simply dummytext of the printin g and typesetting industry.Lorem Ipsum has bee n the industry's standard dummy text.</p>
  <div class="more">READ MORE</div>
</section>
<section class="abs card" style="left:343px">
  <div class="label">CASE STUDIES</div>
  <p>Lorem Ipsum is simply dummytext of the printin g and typesetting industry.Lorem Ipsum has bee n the industry's standard dummy text.</p>
  <div class="more">READ MORE</div>
</section>
<section class="abs card" style="left:623px">
  <div class="label">OUR STORIES</div>
  <p>Lorem Ipsum is simply dummytext of the printin g and typesetting industry.Lorem Ipsum has bee n the industry's standard dummy text.</p>
  <div class="more">READ MORE</div>
</section>

<h1 class="abs welcome-title">Welcome to our mainpage</h1>
<div class="abs welcome-photo" role="img" aria-label="Businessman in a suit walking with papers in hand against a blue sky"></div>
<p class="abs welcome-text">Lorem Ipsum is simply dummy text of the printing and typesettings industry. Lorem Ipsum hasbeen the industry's standard dummy text ever&nbsp; since the 1500s, when an unknown prin ter tooka galley of type and scrambled it to make atype specimen book. It has survived not only five centuries, but also the leap into electronic typesetting, remaining essentially unch anged.&nbsp; It was popularised in the1960s with the release of Letrasetsheets containing Lorem Ipsum passages, and more recentlywith desktop publishing.</p>

<aside class="abs newsletter">
  <span class="t1">NEWSLETTER</span>
  <span class="t2">SIGNUP</span>
  <div class="field">Enter your email id</div>
  <div class="submit">SUBMIT</div>
</aside>

<div class="abs divider"></div>

<section class="abs tabs">
  <div class="tab plain">Why we are</div>
  <div class="tab active">Our Mission</div>
</section>
<div class="abs tab-arrows">
  <span class="arrow-btn"><svg width="5" height="6"><path d="M4 0 1 3l3 3" fill="none" stroke="#fff" stroke-width="1.2"/></svg></span>
  <span class="arrow-btn"><svg width="5" height="6"><path d="M1 0l3 3-3 3" fill="none" stroke="#fff" stroke-width="1.2"/></svg></span>
</div>
<div class="abs mission-photo" role="img" aria-label="Group of business people standing on puzzle pieces"></div>
<p class="abs mission-text">Lorem Ipsums is simply dummy text the printing and typesettings indust Lorem Ipsums has been the industry standar dummy text ever since then 1500s, when an unknown.</p>

<div class="abs calendar">
  <div class="cal-head"><span>&#8249;</span><span>January 2012</span><span>&#8250;</span></div>
  <table>
    <tr><th>MON</th><th>TUE</th><th>WED</th><th>THU</th><th>FRI</th><th>SAT</th><th>SUN</th></tr>
    <tr><td class="other">30</td><td>1</td><td>2</td><td>3</td><td>4</td><td>5</td><td>6</td></tr>
    <tr><td>7</td><td>8</td><td>9</td><td>10</td><td>11</td><td class="today">12</td><td>13</td></tr>
    <tr><td>14</td><td>15</td><td>16</td><td>17</td><td>18</td><td>19</td><td>20</td></tr>
    <tr><td>21</td><td>22</td><td>23</td><td>24</td><td>25</td><td>26</td><td>27</td></tr>
    <tr><td>28</td><td>29</td><td>30</td><td>31</td><td class="other">1</td><td class="other">2</td><td class="other">3</td></tr>
  </table>
</div>

<section class="abs news">
  <h3>Recent News &amp; Events</h3>
  <p class="news-item"><b>During December 2012,</b><br>our Principal&nbsp; Petrophysicist, Martin Keller, has been working on projects for companies.</p>
  <p class="news-item"><b>During November 2013</b><br>our Principal&nbsp; Petrophysicist, Martin Keller, has been working on projects for companies.</p>
</section>
<div class="abs news-arrows">
  <span class="arrow-btn"><svg width="5" height="6"><path d="M4 0 1 3l3 3" fill="none" stroke="#fff" stroke-width="1.2"/></svg></span>
  <span class="arrow-btn"><svg width="5" height="6"><path d="M1 0l3 3-3 3" fill="none" stroke="#fff" stroke-width="1.2"/></svg></span>
</div>

<footer class="abs footer">
  <span class="copy">Copyrights 2013. All Rights Reserved.</span>
  <div class="social" aria-label="Social links"><span></span><span></span><span></span></div>
</footer>
</body>
</html>
```